Business card design for Plumbing and Gas fitting company

We need a business card design for our plumbing and gas fitting company using the company logo and director details. Design should be modern and eye-catching however kept reasonably simple. This design should be targeted at commercial businesses/work so professionalism is key.

Target Market(s)

Commercial/business

Industry/Entity Type

Plumbing

Contact Information for Business Card

Warren Dohey
Director
027 581 9043
warren@vantorplumbingandgas.example
PO Box 7816
Palmerston North 4472

Font styles to use
Sans Serif

Requirements
Must have
• Logo
• Modern
• Kept simple
Nice to have
• Colour scheme based around logo

```html
<!DOCTYPE html>
<html lang="en">
<head>
<meta charset="utf-8">
<title>Vantor Plumbing &amp; Gas – Business Card</title>
<link rel="stylesheet" href="https://fonts.googleapis.com/css2?family=Jost:wght@400;500;600&display=swap">
<style>
  :root {
    --navy: #0b1740;
    --blue: #0a7bc1;
    --orange: #f5821f;
    --white: #ffffff;
    --silver-light: #f2f3f5;
    --silver-mid: #b9bcc2;
    --page: #ffffff;
  }
  * { box-sizing: border-box; margin: 0; padding: 0; }
  html, body {
    width: 1200px; height: 1200px; overflow: hidden;
    background: var(--page);
    font-family: "Jost", sans-serif;
  }
  .canvas { position: relative; width: 1200px; height: 1200px; }
  .card {
    position: absolute; left: 154px;
    width: 899px; height: 513px;
    background: var(--navy);
    overflow: hidden;
  }
  .card--front { top: 46px; }
  .card--back { top: 622px; }

  /* Front */
  .brand {
    position: absolute; left: 149px; top: 150px;
    display: flex; align-items: center; gap: 18px;
  }
  .brand__mark {
    width: 78px; height: 78px; border-radius: 50%;
    background: var(--blue); flex: none;
  }
  .brand__name {
    color: var(--blue); font-weight: 600;
    font-size: 44px; line-height: 1.05;
  }
  .front-decoration {
    position: absolute; left: 555px; top: 66px;
    width: 344px; height: 447px;
    border-top-left-radius: 100% 100%;
    background: linear-gradient(135deg, var(--silver-mid) 0%, var(--silver-light) 45%, var(--silver-mid) 75%, #8f939a 100%);
    opacity: 0.85;
  }

  /* Back */
  .back-brand {
    position: absolute; left: 108px; top: 130px;
    width: 190px; text-align: center;
  }
  .back-brand__mark {
    width: 130px; height: 130px; border-radius: 50%;
    background: var(--blue); margin: 0 auto 16px;
  }
  .back-brand__name {
    color: var(--blue); font-weight: 600;
    font-size: 22px; line-height: 1.15;
  }
  .contact { position: absolute; left: 316px; top: 146px; color: var(--white); }
  .contact__name {
    font-size: 34px; font-weight: 500; letter-spacing: 0.5px; line-height: 1;
  }
  .contact__role {
    color: var(--orange); font-size: 21px; letter-spacing: 4.5px;
    text-align: right; margin-top: 8px; line-height: 1;
  }
  .contact__lines { margin-top: 28px; font-size: 24px; line-height: 1; }
  .contact__line { display: flex; align-items: center; gap: 12px; margin-bottom: 16px; }
  .contact__line svg { width: 20px; height: 20px; fill: var(--white); flex: none; }
  .contact__address { margin-top: 24px; font-size: 24px; line-height: 1.2; }
  .social {
    position: absolute; left: 640px; top: 442px;
    display: flex; gap: 13px;
  }
  .social__slot {
    width: 42px; height: 42px; border-radius: 6px; background: var(--white);
  }
</style>
</head>
<body>
<main class="canvas">
  <section class="card card--front" aria-label="Card front">
    <div class="brand">
      <span class="brand__mark" aria-hidden="true"></span>
      <span class="brand__name">Vantor<br>Plumbing &amp; Gas</span>
    </div>
    <div class="front-decoration" role="img" aria-label="Large brushed silver brand decoration"></div>
  </section>

  <section class="card card--back" aria-label="Card back">
    <div class="back-brand">
      <div class="back-brand__mark" aria-hidden="true"></div>
      <div class="back-brand__name">Vantor<br>Plumbing &amp; Gas</div>
    </div>
    <div class="contact">
      <div class="contact__name">WARREN DOHEY</div>
      <div class="contact__role">DIRECTOR</div>
      <div class="contact__lines">
        <div class="contact__line">
          <svg viewBox="0 0 24 24" aria-hidden="true"><path d="M6.6 10.8a15.1 15.1 0 0 0 6.6 6.6l2.2-2.2c.3-.3.7-.4 1-.2 1.1.4 2.3.6 3.6.6.6 0 1 .4 1 1V20c0 .6-.4 1-1 1A17 17 0 0 1 3 4c0-.6.4-1 1-1h3.5c.6 0 1 .4 1 1 0 1.3.2 2.5.6 3.6.1.3 0 .7-.2 1z"/></svg>
          <span>027 581 9043</span>
        </div>
        <div class="contact__line">
          <svg viewBox="0 0 24 24" aria-hidden="true"><path d="M2 5h20v14H2z M2 5l10 8 10-8" fill="none" stroke="#fff" stroke-width="2"/></svg>
          <span>warren@vantorplumbingandgas.example</span>
        </div>
      </div>
      <div class="contact__address">PO Box 7816<br>Palmerston North 4472</div>
    </div>
    <div class="social" aria-label="Social links">
      <span class="social__slot"></span>
      <span class="social__slot"></span>
      <span class="social__slot"></span>
      <span class="social__slot"></span>
    </div>
  </section>
</main>
</body>
</html>
```